Federal IT Consulting Company - Bridgemont Consulting Group

We're seeking a skilled web designer to create a modern, bold, and engaging WordPress website for Bridgemont Consulting Group, LLC. Our company specializes in federal IT consulting, and our name is a play on "Bridging Momentum." The website should reflect our expertise in the federal technology marketplace and position us as a trusted partner for clients navigating their IT journey.

contact: info@bridgemontgrp.com

Current Status

WordPress is already installed on our hosting account
We have an existing logo (may need modernization)

Design Requirements

Style:

Modern and visually striking design
Bold elements to convey confidence and expertise
Incorporate the concept of "bridging momentum" into the design

Features:

Modern UX sliders for dynamic content presentation
Eye-catching, high-quality images (stock photos to be sourced by the designer)
Responsive design for all devices

Color Scheme:

To be proposed by the designer, should align with our brand and convey trust and technological expertise

Logo:

Evaluate our current logo
Create a transparent background version if needed
Propose modernization if deemed necessary

Accessibility:

Ensure design elements are accessible to users with disabilities
Use high contrast ratios for text and background colors
Provide text alternatives for non-text content

Website Structure
Create the following pages, with the possibility of subpages:

Home
Services
About
Contact

Specific Page Requirements
Home Page

Striking hero section with a clear value proposition
Overview of our services
Client testimonials or trust indicators

Services Page

Detailed list of our IT consulting services
Clear explanation of how we help navigate the federal IT landscape

About Page

Company history and mission
Team highlights (if applicable)
Our approach to federal IT consulting

Contact Page

Contact form
Other contact methods (phone, email)

Technical Requirements

Fully responsive design
SEO best practices implemented
Fast loading times
Integration with necessary plugins (to be discussed)
Training on how to update and maintain the site
Full compliance with Web Content Accessibility Guidelines (WCAG) 2.1 Level AA
Adherence to Section 508 standards for federal website accessibility
Implementation of necessary features for ADA compliance
Updates

Designs look the same

Target Market(s)

US Federal Govt customers looking for IT support.

Industry/Entity Type

IT Consulting

Coding

Coded - Design and coding required

Colors
0054AA
0677BA
7BADD7
CADEEF
E8F1F8
0094D4
00A9DD
6FCCEA
C7EBF8
E9F6FB
00AB8E
00BBA5
67D7C9
C6EFE9
E9F9F6

```html
<!DOCTYPE html>
<html lang="en">
<head>
<meta charset="utf-8">
<title>Bridgemont Federal Services — Federal IT Consulting</title>
<link rel="stylesheet" href="https://fonts.googleapis.com/css2?family=Syncopate:wght@700&family=Open+Sans:ital,wght@0,400;0,600;0,700;1,400&display=swap">
<style>
  :root {
    --accent: #00b7f1;
    --accent-deep: #0094d4;
    --ink: #111111;
    --text: #3a3a3a;
    --white: #ffffff;
    --rail: #000000;
    --dark: #1e1f20;
    --footer: #1b1c1d;
    --hero-a: #061a3a;
    --hero-b: #0b4a7a;
    --hero-c: #19a6d6;
  }
  * { box-sizing: border-box; margin: 0; padding: 0; }
  html, body { width: 1200px; height: 2616px; overflow: hidden; }
  body { position: relative; background: var(--white); font-family: "Open Sans", Arial, sans-serif; color: var(--text); }
  .abs { position: absolute; }
  .display { font-family: "Syncopate", "Arial Black", sans-serif; font-weight: 700; text-transform: uppercase; }
  .btn { position: absolute; display: flex; align-items: center; justify-content: center; background: var(--accent); color: var(--white); font-weight: 700; font-size: 16px; text-decoration: none; }

  /* Hero */
  .hero { position: absolute; left: 0; top: 0; width: 1200px; height: 600px; background: var(--hero-a); overflow: hidden; }
  .hero-photo { position: absolute; left: 90px; top: 0; width: 1110px; height: 600px;
    background: radial-gradient(ellipse 420px 300px at 820px 310px, var(--hero-c) 0%, rgba(25,166,214,0.35) 45%, transparent 75%),
                linear-gradient(120deg, var(--hero-a) 0%, #0a2d5a 40%, var(--hero-b) 75%, #0d6f9f 100%); }
  .hero-rail { position: absolute; left: 0; top: 0; width: 90px; height: 600px; background: var(--rail); }
  .brand { position: absolute; display: flex; align-items: center; gap: 10px; color: var(--white); font-weight: 700; font-size: 19px; line-height: 1.15; letter-spacing: 0.5px; }
  .brand-dot { width: 34px; height: 34px; border-radius: 50%; background: var(--white); flex: none; }
  .nav { position: absolute; left: 524px; top: 70px; display: flex; gap: 36px; font-size: 16px; color: var(--white); }
  .nav .current { font-weight: 700; }
  .hero-title { position: absolute; left: 112px; top: 190px; font-size: 49px; line-height: 52px; color: var(--white); letter-spacing: 1px; }
  .hero-title .hl { color: var(--accent); }
  .hero-lead { position: absolute; left: 112px; top: 370px; width: 480px; font-size: 17px; line-height: 28px; color: var(--white); font-weight: 600; }
  .rail-dot { position: absolute; left: 49px; width: 7px; height: 7px; border-radius: 50%; background: var(--white); }

  /* About */
  .about-photo { position: absolute; left: 111px; top: 669px; width: 402px; height: 517px;
    background: radial-gradient(circle 140px at 200px 150px, rgba(0,183,241,0.7), transparent 70%), linear-gradient(160deg, #5d7f9e 0%, #243c57 55%, #0d1a2a 100%); }
  .section-title { font-size: 40px; line-height: 1; color: var(--ink); }
  .section-title .hl { color: var(--accent); }
  .about-body { position: absolute; left: 592px; top: 783px; width: 505px; font-size: 15px; line-height: 28.4px; }
  .about-body p { margin-bottom: 12px; }
  .about-body .lead { font-weight: 700; color: var(--ink); }

  /* Services */
  .services { position: absolute; left: 0; top: 1272px; width: 1200px; height: 548px; background: var(--dark); color: var(--white); text-align: center; }
  .services .section-title { color: var(--white); margin-top: 64px; }
  .services .sub { margin-top: 22px; font-size: 16px; }
  .service { position: absolute; top: 220px; width: 230px; }
  .service svg { display: block; margin: 0 auto; }
  .service h3 { margin-top: 18px; font-size: 17px; line-height: 25px; color: var(--accent); letter-spacing: 0.5px; }
  .service p { margin-top: 8px; font-size: 16px; line-height: 27.5px; color: var(--white); }

  /* Testimonials */
  .testimonials { position: absolute; left: 0; top: 1820px; width: 1200px; height: 504px; text-align: center; }
  .testimonials .section-title { margin-top: 84px; line-height: 52px; }
  .quote { margin: 34px auto 0; width: 800px; font-style: italic; font-size: 30px; line-height: 43px; color: var(--text); }
  .author { margin-top: 28px; font-size: 17px; }
  .dots { position: absolute; left: 564px; top: 428px; display: flex; align-items: center; gap: 18px; }
  .dot { width: 8px; height: 8px; border-radius: 50%; background: var(--ink); }

  /* Footer */
  .footer { position: absolute; left: 0; top: 2324px; width: 1200px; height: 292px; background: var(--footer); color: var(--white); font-size: 16px; line-height: 28.4px; }
  .footer h4 { font-size: 15px; color: var(--accent); letter-spacing: 0.5px; margin-bottom: 14px; }
  .footer a { color: var(--accent); }
  .fcol { position: absolute; top: 60px; }
  .fcol ul { list-style: none; padding-left: 4px; }
</style>
</head>
<body>

<header class="hero">
  <div class="hero-photo" role="img" aria-label="Glowing digital padlock on a circuit board with cybersecurity interface graphics"></div>
  <div class="hero-rail"></div>
  <svg class="abs" style="left:36px;top:256px" width="32" height="32" viewBox="0 0 32 32" aria-hidden="true">
    <circle cx="16" cy="16" r="12" fill="none" stroke="#00b7f1" stroke-width="3"/>
    <circle cx="16" cy="16" r="6" fill="#ffffff"/>
  </svg>
  <span class="rail-dot" style="top:311px"></span>
  <span class="rail-dot" style="top:354px"></span>

  <div class="brand" style="left:112px;top:48px"><span class="brand-dot"></span><span>Bridgemont<br>Federal Services</span></div>
  <nav class="nav"><span class="current">Home</span><span>About Us</span><span>Our Services</span><span>Contact Us</span></nav>
  <a class="btn" style="left:935px;top:56px;width:155px;height:50px">Get in Quote</a>

  <h1 class="hero-title display">Specializes<br>in Federal<br><span class="hl">IT Consulting</span></h1>
  <p class="hero-lead">Sed ut perspiciatis unde omnis iste natus erroluptatem accusantium doloremque laudantium</p>
  <a class="btn" style="left:112px;top:464px;width:348px;height:50px;font-size:15px">Schedule Your Free Consultation Today</a>
</header>

<section>
  <div class="about-photo" role="img" aria-label="Two IT consultants reviewing a laptop in a server room"></div>
  <h2 class="section-title display abs" style="left:592px;top:714px">About <span class="hl">Us</span></h2>
  <div class="about-body">
    <p class="lead">Lorem ipsum dolor sit amet, consectetur adipiscing elit, sed ei usmod tempor incididunt ut labore et dolore magna aliqa.</p>
    <p>Lorem ipsum dolor sit amet, consectetur adipiscing elit, sed eiusmod tempor incididunt ut labore et dolore magna aliqa. Ut enim ad minim veniam, quis nostrud exercitation ullamco laboris nisi ut aliquip ex ea commodo consequat. Duis aute irure dolor in reprederit in voluptate velit esse cillum dolore eu fugiat nulla pariatur.</p>
    <p>Lorem ipsum dolor sit amet, consectetur adipiscing elit, sed eiusmod tempor incididunt ut labore et dolore magna aliqa.</p>
  </div>
  <a class="btn" style="left:592px;top:1086px;width:154px;height:50px">Learn More</a>
</section>

<section class="services">
  <h2 class="section-title display">Our <span class="hl">Services</span></h2>
  <p class="sub">Explore our specialized services designed to safeguard your assets</p>

  <div class="service" style="left:104px">
    <svg width="60" height="60" viewBox="0 0 60 60" fill="none" stroke="#fff" stroke-width="2.2" aria-hidden="true">
      <circle cx="17" cy="17" r="13"/><circle cx="17" cy="13" r="4"/><path d="M9 25c2-5 14-5 16 0"/>
      <circle cx="43" cy="17" r="13"/><circle cx="43" cy="13" r="4"/><path d="M35 25c2-5 14-5 16 0"/>
      <circle cx="17" cy="43" r="13"/><path d="M11 43l4 4 8-8"/>
      <circle cx="43" cy="43" r="13"/><circle cx="43" cy="39" r="4"/><path d="M35 51c2-5 14-5 16 0"/>
    </svg>
    <h3 class="display">IT Staff Augmentation</h3>
    <p>Lorem ipsum dolor sit amet, consectetur adipiscing elit, sed do onsectetur adipiscing elit, sed do eiusmod</p>
  </div>

  <div class="service" style="left:359px">
    <svg width="80" height="60" viewBox="0 0 80 60" fill="none" stroke="#fff" stroke-width="2.2" aria-hidden="true">
      <rect x="3" y="3" width="62" height="40" rx="2"/><path d="M3 36h62M28 43l-3 10h18l-3-10M20 53h28"/>
      <path d="M22 14l-7 6 7 6M44 14l7 6-7 6M37 11l-8 18"/>
      <circle cx="64" cy="40" r="9"/><circle cx="64" cy="40" r="3.5"/>
    </svg>
    <h3 class="display">Dedicated Dev Teams</h3>
    <p>Lorem ipsum dolor sit amet, consectetur adipiscing elit, sed do onsectetur adipiscing elit, sed do eiusmod</p>
  </div>

  <div class="service" style="left:613px">
    <svg width="60" height="60" viewBox="0 0 60 60" fill="none" stroke="#fff" stroke-width="2.2" aria-hidden="true">
      <path d="M14 3h28l12 12v42H14z"/><path d="M42 3v12h12"/>
      <path d="M34 22h14M36 29h12M38 36h10M30 44h18"/>
      <circle cx="18" cy="32" r="12"/><circle cx="18" cy="29" r="4"/><path d="M11 39c2-4 12-4 14 0"/><path d="M27 41l8 8"/>
    </svg>
    <h3 class="display">Tech Recruitment</h3>
    <p>Lorem ipsum dolor sit amet, consectetur adipiscing elit, sed do onsectetur adipiscing elit, sed do eiusmod</p>
  </div>

  <div class="service" style="left:867px">
    <svg width="60" height="60" viewBox="0 0 60 60" fill="none" stroke="#fff" stroke-width="2.2" aria-hidden="true">
      <path d="M4 10h22M34 10h22M4 30h36M48 30h8M4 50h8M20 50h36"/>
      <circle cx="30" cy="10" r="4"/><circle cx="44" cy="30" r="4"/><circle cx="16" cy="50" r="4"/>
    </svg>
    <h3 class="display">Custom IT Staffing</h3>
    <p>Lorem ipsum dolor sit amet, consectetur adipiscing elit, sed do onsectetur adipiscing elit, sed do eiusmod</p>
  </div>
</section>

<section class="testimonials">
  <h2 class="section-title display">Client<br><span class="hl">Testimonials</span></h2>
  <p class="quote">“Sed ut perspiciatis unde omnis iste natus error sit vo luptatem accusantium doloremque laudantium, totam rem lorem ipsum aperiam"</p>
  <p class="author">– Dana Whitfield</p>
  <div class="dots">
    <svg width="28" height="28" viewBox="0 0 28 28" aria-hidden="true">
      <circle cx="14" cy="14" r="11" fill="none" stroke="#00b7f1" stroke-width="3"/>
      <circle cx="14" cy="14" r="6" fill="#111"/>
    </svg>
    <span class="dot"></span><span class="dot"></span>
  </div>
</section>

<footer class="footer">
  <div class="brand" style="left:112px;top:62px;font-size:24px"><span class="brand-dot" style="width:40px;height:40px"></span><span>Bridgemont<br>Federal Services</span></div>
  <p class="abs" style="left:111px;top:190px">2024 Bridgemont Federal Services, LLC.<br>All Rights Reserved.</p>

  <div class="fcol" style="left:455px">
    <h4 class="display">Contact</h4>
    <ul>
      <li>ADDRESS:Bridgemont federal,</li>
      <li>address comes hete</li>
      <li>PHONE:<a>+1 (555) 014-2290</a></li>
      <li>EMAIL:<a>info@bridgemontgrp.com</a></li>
    </ul>
  </div>
  <div class="fcol" style="left:729px">
    <h4 class="display">Quick Links</h4>
    <ul><li>Home</li><li>About Us</li><li>Our Services</li><li>Testimonials</li></ul>
  </div>
  <div class="fcol" style="left:943px">
    <h4 class="display">Other Links</h4>
    <ul><li>Testimonials</li><li>Privacy Policy</li><li>Terms &amp; Conditions</li><li>Contact</li></ul>
  </div>
</footer>

</body>
</html>
```